Redesign and move to Wordpress for quarvendo.com

Our website needs a redesign and at the same time we are moving it to Wordpress. Please help us with a new digital professional look and feel.

We are an Australian Software Engineering company specialising in advanced software development using in A.I., PLatform Engineering, Integration and Cloud. See the current quarvendo.com for more information about us.

```html
<!DOCTYPE html>
<html lang="en">
<head>
<meta charset="utf-8">
<title>Quarvendo — Reliable Smart Software Engineering</title>
<link rel="stylesheet" href="https://fonts.googleapis.com/css2?family=Audiowide&family=Jost:wght@400;500;600&display=swap">
<style>
:root{
  --navy:#0b1a45;
  --navy-deep:#08122f;
  --blue:#1a4a8a;
  --teal:#4fc1b4;
  --teal-light:#e6f5f3;
  --ink:#2b2f3a;
  --muted:#666c78;
  --line:#d9dde5;
  --card-top:#eef3fa;
  --white:#ffffff;
  --display:"Audiowide",sans-serif;
  --body:"Jost",sans-serif;
}
*{box-sizing:border-box;margin:0;padding:0}
html,body{width:1200px;height:3987px;overflow:hidden;background:var(--white)}
body{font-family:var(--body);color:var(--ink)}
.page{position:relative;width:1200px;height:3987px;overflow:hidden}
.abs{position:absolute}

/* header + hero */
.hero{left:0;top:0;width:1200px;height:715px;background:linear-gradient(100deg,var(--navy-deep) 0%,#0c2358 45%,#0f3d86 75%,#0a2a66 100%)}
.hero-visual{left:520px;top:60px;width:680px;height:655px;background:radial-gradient(ellipse at 45% 45%,#3fa8ff 0%,#1663c4 30%,#0c2f73 65%,rgba(8,18,47,0) 100%);opacity:.9}
.brand{display:flex;align-items:center;gap:14px;color:var(--white);font-family:var(--display);font-size:30px;letter-spacing:1px;white-space:nowrap}
.brand-mark{width:40px;height:40px;border:3px solid var(--teal)}
.site-brand{left:88px;top:31px}
.nav{left:534px;top:46px;display:flex;gap:26px;align-items:center;font-size:13px;color:var(--white);text-transform:uppercase;font-weight:500}
.search{left:895px;top:36px;width:216px;height:40px;display:flex}
.search span{flex:1;background:#2a3656;color:#aab3c6;font-size:12px;padding:12px 22px}
.search i{width:38px;background:var(--teal);display:flex;align-items:center;justify-content:center}
.hero-title{left:86px;top:262px;font-family:var(--display);font-size:54px;line-height:63px;color:var(--white);white-space:nowrap}
.hero-title em{font-style:normal;color:var(--teal)}

/* about */
.photo{border:0;box-shadow:0 14px 24px rgba(0,0,0,.15)}
.about-title{left:619px;top:792px;font-family:var(--display);font-size:41px;color:var(--navy);white-space:nowrap}
.about-text{left:620px;top:852px;width:440px;font-size:15px;line-height:20.5px;color:#444}
.link-more{font-size:11px;font-weight:600;color:var(--teal);letter-spacing:.5px;display:flex;align-items:center;gap:8px;text-transform:uppercase;white-space:nowrap}

/* services */
.section-title{width:1200px;text-align:center;font-family:var(--display);color:var(--navy)}
.service{border:1px solid #7d9ed0;background:linear-gradient(180deg,var(--card-top),#fff);display:flex;flex-direction:column;align-items:center;justify-content:center;text-align:center;font-family:var(--display);font-size:14px;color:var(--navy);line-height:19px;padding:0 20px}
.service svg{margin-bottom:14px}
.service .go{position:absolute;right:-1px;bottom:-1px;width:26px;height:26px;background:var(--blue);display:flex;align-items:center;justify-content:center}
.service.featured{background:var(--teal-light);border-color:var(--teal-light)}
.service.featured .go{background:var(--teal)}
.service .wordmark{font-size:26px;color:var(--blue);margin-bottom:20px}

/* news */
.news-band{left:0;top:1856px;width:1200px;height:477px;background:linear-gradient(180deg,#0c2a66,#12397c 60%,#0b2a63)}
.news-title{top:1950px;font-size:42px;color:var(--white)}
.news-sub{top:2005px;width:1200px;text-align:center;font-family:var(--display);font-size:17px;color:var(--white)}
.article{width:325px;height:494px;top:2082px;background:var(--white);box-shadow:0 10px 30px rgba(0,0,0,.12)}
.article-img{position:absolute;left:0;top:12px;width:325px;height:256px}
.article-body{position:absolute;left:30px;top:290px;width:272px}
.article h3{font-family:var(--display);font-weight:400;font-size:14px;line-height:19px;color:var(--navy);height:48px}
.tags{font-size:10px;font-weight:600;color:var(--navy);margin-top:8px}
.tags b{color:var(--teal);margin:0 4px}
.excerpt{font-size:11.5px;line-height:17px;color:#555;margin-top:8px;height:56px}
.meta{border-top:1px solid var(--line);margin-top:20px;padding-top:12px;font-size:12px;color:#555;display:flex;gap:10px;align-items:center}

/* booking */
.book-line{top:2712px;width:1200px;text-align:center;font-family:var(--display);font-size:15px;color:var(--navy)}
.booking{left:147px;top:2762px;width:904px;height:537px;border:1px solid #2d4d86;background:var(--white)}
.booking-side{position:absolute;left:0;top:0;width:317px;height:535px;background:var(--teal);color:var(--white);padding:30px}
.booking-side h4{font-weight:500;font-size:25px;margin-top:56px}
.side-row{display:flex;gap:10px;align-items:center;font-size:12px;margin-top:20px;font-weight:500}
.dot{width:18px;height:18px;border-radius:50%;background:var(--white);flex:none}
.cal{position:absolute;left:0;top:0;width:902px;height:535px}
.cal p,.cal span{white-space:nowrap}
.cal-day{position:absolute;width:34px;height:34px;margin-left:-17px;margin-top:-17px;display:flex;align-items:center;justify-content:center;font-size:12px;color:#333;border-radius:50%}
.cal-day.avail{background:#dfe9f6;color:var(--blue);font-weight:600}
.cal-day.picked{background:var(--blue);color:#fff;font-weight:600}
.slot{position:absolute;left:703px;width:156px;height:43px;border:1.5px solid var(--blue);border-radius:4px;display:flex;align-items:center;justify-content:center;font-size:15px;font-weight:600;color:var(--blue)}

/* partners */
.partner{top:3397px;font-size:34px;font-weight:600;color:#8b8f96;display:flex;align-items:center;gap:12px;white-space:nowrap}
.partner i{width:44px;height:44px;background:#8b8f96;display:block}

/* footer */
.footer{left:0;top:3511px;width:1200px;height:476px;background:linear-gradient(180deg,#0b2058,#0a1a4a)}
.news-head{left:88px;top:3572px;font-family:var(--display);font-size:23px;line-height:29px;color:var(--white);white-space:nowrap}
.news-reg{left:88px;top:3632px;font-family:var(--display);font-size:13px;color:var(--white);white-space:nowrap}
.email{left:689px;top:3588px;width:314px;height:45px;background:var(--white);font-size:12px;color:#555;padding:14px 20px}
.subscribe{left:1003px;top:3588px;width:107px;height:45px;background:var(--teal);color:var(--white);font-size:12px;font-weight:600;display:flex;align-items:center;justify-content:center}
.rule{left:88px;top:3703px;width:1024px;height:1px;background:rgba(255,255,255,.18)}
.social{top:3817px;width:45px;height:45px;background:#2b3d6c;color:var(--white);font-size:14px;font-weight:600;display:flex;align-items:center;justify-content:center}
.small{font-size:12px;color:var(--white);white-space:nowrap}
</style>
</head>
<body>
<div class="page">

  <!-- hero -->
  <div class="abs hero"></div>
  <div class="abs hero-visual" role="img" aria-label="Robotic hand touching a glowing holographic interface above a laptop"></div>
  <div class="abs brand site-brand"><span class="brand-mark"></span>quarvendo</div>
  <nav class="abs nav">
    <svg width="16" height="15" viewBox="0 0 16 15"><path d="M8 1 1 7h2v7h4V10h2v4h4V7h2z" fill="var(--teal)"/></svg>
    <span>Services</span><span>Contact</span><span>About</span><span>Blog</span>
  </nav>
  <div class="abs search"><span>Search here...</span><i><svg width="14" height="14" viewBox="0 0 14 14"><circle cx="6" cy="6" r="4.5" stroke="#fff" stroke-width="1.6" fill="none"/><path d="m9.5 9.5 3 3" stroke="#fff" stroke-width="1.6"/></svg></i></div>
  <h1 class="abs hero-title">Reliable Smart<br><em>Software</em><br>Engineering</h1>

  <!-- about -->
  <div class="abs photo" style="left:149px;top:650px;width:196px;height:132px;background:linear-gradient(135deg,#c9ccd2,#7d8490)" role="img" aria-label="Robot hand typing on a keyboard"></div>
  <div class="abs photo" style="left:370px;top:650px;width:195px;height:263px;background:linear-gradient(160deg,#9fd4e8,#3c8fb5)" role="img" aria-label="Person wearing a virtual reality headset with data charts"></div>
  <div class="abs photo" style="left:149px;top:805px;width:196px;height:263px;background:linear-gradient(160deg,#3a7fb0,#173c66)" role="img" aria-label="Business professional holding a tablet with data overlays"></div>
  <div class="abs photo" style="left:370px;top:937px;width:195px;height:131px;background:linear-gradient(135deg,#2b5d9a,#0b1f45)" role="img" aria-label="Hands typing on a keyboard with a digital glow"></div>
  <h2 class="abs about-title">At Quarvendo</h2>
  <p class="abs about-text">At Quarvendo, we craft bespoke software solutions that are not available on the market. By building organizations market-leading products, process automation, legacy system enablement, or advanced intelligent systems, we empower our customers to achieve a competitive edge in their industry.</p>
  <div class="abs link-more" style="left:620px;top:980px">Read more <svg width="18" height="10" viewBox="0 0 18 10"><path d="M1 5h15M12 1l4 4-4 4" stroke="var(--teal)" stroke-width="1.4" fill="none"/></svg></div>

  <!-- services -->
  <h2 class="abs section-title" style="top:1168px;font-size:42px">Our Services</h2>

  <div class="abs service" style="left:99px;top:1254px;width:230px;height:153px">
    <svg width="60" height="60" viewBox="0 0 60 60" fill="none" stroke="var(--navy)" stroke-width="2"><path d="M30 8c10 0 17 7 17 16 0 5-2 8-4 10v8h-8v8"/><circle cx="26" cy="18" r="3"/><circle cx="20" cy="30" r="3"/><circle cx="30" cy="34" r="3"/><path d="M26 21v6M23 30h4M30 37v8"/><circle cx="30" cy="48" r="3" fill="var(--navy)"/></svg>
    CoPilot / AI Agents<span class="go"><svg width="8" height="10" viewBox="0 0 8 10"><path d="m2 1 4 4-4 4" stroke="#fff" stroke-width="1.5" fill="none"/></svg></span>
  </div>
  <div class="abs service" style="left:99px;top:1433px;width:230px;height:305px">
    <svg width="96" height="80" viewBox="0 0 96 80" fill="none" stroke="var(--navy)" stroke-width="2.5"><circle cx="48" cy="40" r="9"/><circle cx="18" cy="40" r="8"/><circle cx="78" cy="40" r="8"/><circle cx="48" cy="10" r="6"/><circle cx="40" cy="70" r="6"/><circle cx="60" cy="70" r="6"/><path d="M26 40h13M57 40h13M48 16v15M44 49l-3 15M52 49l4 15"/></svg>
    Microservices<span class="go"><svg width="8" height="10" viewBox="0 0 8 10"><path d="m2 1 4 4-4 4" stroke="#fff" stroke-width="1.5" fill="none"/></svg></span>
  </div>

  <div class="abs service" style="left:354px;top:1255px;width:230px;height:305px">
    <svg width="80" height="80" viewBox="0 0 80 80" fill="none" stroke="var(--navy)" stroke-width="2.5"><circle cx="14" cy="10" r="6" fill="var(--navy)"/><circle cx="40" cy="10" r="6"/><circle cx="66" cy="10" r="6"/><circle cx="14" cy="40" r="6"/><circle cx="40" cy="40" r="6" fill="var(--navy)"/><circle cx="66" cy="40" r="6"/><circle cx="14" cy="70" r="6"/><circle cx="40" cy="70" r="6"/><circle cx="66" cy="70" r="6" fill="var(--navy)"/><path d="M20 40h14M46 40h14"/></svg>
    Enterprise Systems Integration<span class="go"><svg width="8" height="10" viewBox="0 0 8 10"><path d="m2 1 4 4-4 4" stroke="#fff" stroke-width="1.5" fill="none"/></svg></span>
  </div>
  <div class="abs service" style="left:354px;top:1587px;width:230px;height:151px">
    <svg width="70" height="66" viewBox="0 0 70 66" fill="none" stroke="var(--navy)" stroke-width="2.5"><rect x="14" y="2" width="30" height="12" rx="3"/><rect x="4" y="28" width="30" height="12" rx="3"/><rect x="14" y="52" width="30" height="12" rx="3"/><path d="M29 14v14M19 40v6h10v6"/><path d="M48 34l10-8 10 8-10 8z" fill="var(--blue)" stroke="var(--blue)"/><path d="M34 34h14"/></svg>
    iPaaS<span class="go"><svg width="8" height="10" viewBox="0 0 8 10"><path d="m2 1 4 4-4 4" stroke="#fff" stroke-width="1.5" fill="none"/></svg></span>
  </div>

  <div class="abs service" style="left:610px;top:1255px;width:230px;height:154px">
    <svg width="76" height="60" viewBox="0 0 76 60" fill="none" stroke="var(--navy)" stroke-width="2.2"><path d="M20 34a12 12 0 0 1 2-24 16 16 0 0 1 30 2 11 11 0 0 1 4 22"/><circle cx="38" cy="30" r="4" fill="var(--navy)"/><circle cx="28" cy="28" r="3"/><circle cx="48" cy="28" r="3"/><path d="M38 34v12M28 31v10M48 31v10"/><circle cx="38" cy="50" r="4" fill="var(--navy)"/></svg>
    PLatform Enginee..<span class="go"><svg width="8" height="10" viewBox="0 0 8 10"><path d="m2 1 4 4-4 4" stroke="#fff" stroke-width="1.5" fill="none"/></svg></span>
  </div>
  <div class="abs service featured" style="left:610px;top:1433px;width:230px;height:305px">
    <div class="wordmark">Glidex</div>
    Custom<br>Integration for<br>Small to Medium<br>Business<span class="go"><svg width="8" height="10" viewBox="0 0 8 10"><path d="m2 1 4 4-4 4" stroke="#fff" stroke-width="1.5" fill="none"/></svg></span>
  </div>

  <div class="abs service" style="left:865px;top:1255px;width:230px;height:305px">
    <svg width="80" height="76" viewBox="0 0 80 76" fill="none" stroke="var(--navy)" stroke-width="2.5"><path d="M30 14a26 26 0 1 0 30 40"/><path d="M22 22l-6-4M16 38H8M22 56l-6 5"/><path d="M48 70V34h-10l16-18 16 18H60v36z" fill="var(--blue)" stroke="var(--blue)"/></svg>
    REal-time DATA<br>Stream<br>PROCESSING<span class="go"><svg width="8" height="10" viewBox="0 0 8 10"><path d="m2 1 4 4-4 4" stroke="#fff" stroke-width="1.5" fill="none"/></svg></span>
  </div>
  <div class="abs service" style="left:865px;top:1587px;width:230px;height:151px">
    <svg width="76" height="66" viewBox="0 0 76 66" fill="none" stroke="var(--navy)" stroke-width="2.2"><rect x="4" y="16" width="36" height="40" rx="6"/><path d="M14 56v8l8-8"/><path d="M40 36h8l6 8v-8a14 14 0 1 0-26-14"/><path d="M14 28v8M14 42h0" stroke-width="3"/></svg>
    Conversational AI<span class="go"><svg width="8" height="10" viewBox="0 0 8 10"><path d="m2 1 4 4-4 4" stroke="#fff" stroke-width="1.5" fill="none"/></svg></span>
  </div>

  <!-- news -->
  <div class="abs news-band" role="img" aria-label="Dark blue circuit board pattern background"></div>
  <h2 class="abs section-title news-title">News &amp; Articles</h2>
  <div class="abs news-sub">Updates from our industry</div>

  <article class="abs article" style="left:96px">
    <div class="article-img" style="background:linear-gradient(180deg,#1d5a48,#0e2f4a 60%,#2a7fc9)" role="img" aria-label="Rows of server racks in a data centre"></div>
    <div class="article-body">
      <h3>Why most upgrade paths for FlowLink lead to using...</h3>
      <div class="tags">Integration<b>•</b>FlowLink</div>
      <p class="excerpt">Introduction In today's fast-evolving technological landscape, businesses are increasingly seeking r...</p>
      <div class="meta"><svg width="12" height="12" viewBox="0 0 12 12"><rect x="1" y="2" width="10" height="9" fill="none" stroke="#999"/></svg>June 24, 2024</div>
    </div>
  </article>
  <article class="abs article" style="left:437px">
    <div class="article-img" style="background:linear-gradient(150deg,#5f6f76,#1f2b33 55%,#c9a46a)" role="img" aria-label="Computer monitor glowing on a desk"></div>
    <div class="article-body">
      <h3>How to get visibility into your FlowLink environment</h3>
      <div class="tags">Integration<b>•</b>FlowLink<b>•</b>Business Insights</div>
      <p class="excerpt">In today's fast-paced business environment, the ability to monitor and understand the flow of data w...</p>
      <div class="meta"><svg width="12" height="12" viewBox="0 0 12 12"><rect x="1" y="2" width="10" height="9" fill="none" stroke="#999"/></svg>June 24, 2024</div>
    </div>
  </article>
  <article class="abs article" style="left:777px">
    <div class="article-img" style="background:linear-gradient(160deg,#c9b6bf,#7b6a78 60%,#4d4350)" role="img" aria-label="Abandoned office building with old filing cabinets"></div>
    <div class="article-body">
      <h3>Why is FlowLink Dead?</h3>
      <div class="tags">Integration<b>•</b>FlowLink<b>•</b>Corvalis<b>•</b>Cirrus</div>
      <p class="excerpt">In the ever-evolving world of technology, keeping up with the latest advancements is not just a stra...</p>
      <div class="meta"><svg width="12" height="12" viewBox="0 0 12 12"><rect x="1" y="2" width="10" height="9" fill="none" stroke="#999"/></svg>June 24, 2024</div>
    </div>
  </article>

  <div class="abs link-more" style="left:537px;top:2624px">View all article <svg width="18" height="10" viewBox="0 0 18 10"><path d="M1 5h15M12 1l4 4-4 4" stroke="var(--teal)" stroke-width="1.4" fill="none"/></svg></div>

  <!-- booking -->
  <div class="abs book-line">Book an obligation free consultation with our Lead Technologist</div>
  <div class="abs booking">
    <div class="booking-side">
      <span style="display:block;width:52px;height:52px;border:3px solid #fff"></span>
      <h4>60 Minute Meeting ⌄</h4>
      <div class="side-row"><span class="dot"></span>60 min</div>
      <div class="side-row"><span class="dot"></span>Web conferencing details provided upon confirmation.</div>
      <p style="font-size:12px;margin-top:26px;line-height:16px">A preliminary discussion with one of our digital advertising specialists at Lumen Depot</p>
      <p style="position:absolute;left:30px;bottom:28px;font-size:13px;font-weight:600">Cookie Setting</p>
    </div>
    <div class="cal">
      <p class="abs" style="left:360px;top:28px;font-size:16px;color:#333">Select a Date &amp; Time</p>
      <span class="abs" style="left:418px;top:78px;width:26px;height:26px;border-radius:50%;background:#e4e6ea;display:flex;align-items:center;justify-content:center;font-size:12px">‹</span>
      <p class="abs" style="left:460px;top:83px;font-size:12px;color:#333">September 2025</p>
      <span class="abs" style="left:584px;top:78px;width:26px;height:26px;border-radius:50%;background:var(--navy);color:#fff;display:flex;align-items:center;justify-content:center;font-size:12px">›</span>
      <p class="abs" style="left:703px;top:83px;font-size:12px;color:#555">Friday September 27</p>

      <div class="abs" style="left:0;top:0;width:902px;height:535px;font-size:10px;color:#555">
        <span class="abs" style="left:364px;top:136px">MON</span><span class="abs" style="left:412px;top:136px">TUE</span><span class="abs" style="left:456px;top:136px">WED</span><span class="abs" style="left:503px;top:136px">THU</span><span class="abs" style="left:554px;top:136px">FRI</span><span class="abs" style="left:600px;top:136px">SAT</span><span class="abs" style="left:645px;top:136px">SUN</span>
      </div>
      <div class="cal-day" style="left:656px;top:167px">1</div>
      <div class="cal-day" style="left:373px;top:209px">2</div><div class="cal-day" style="left:420px;top:209px">3</div><div class="cal-day" style="left:468px;top:209px">4</div><div class="cal-day" style="left:514px;top:209px">5</div><div class="cal-day" style="left:562px;top:209px">6</div><div class="cal-day" style="left:610px;top:209px">7</div><div class="cal-day" style="left:656px;top:212px">8</div>
      <div class="cal-day" style="left:373px;top:252px">9</div><div class="cal-day" style="left:420px;top:252px">10</div><div class="cal-day" style="left:468px;top:252px">11</div><div class="cal-day" style="left:514px;top:252px">12</div><div class="cal-day" style="left:562px;top:252px">13</div><div class="cal-day" style="left:610px;top:252px">14</div><div class="cal-day" style="left:656px;top:255px">15</div>
      <div class="cal-day" style="left:373px;top:297px">16</div><div class="cal-day" style="left:420px;top:297px">17</div><div class="cal-day" style="left:468px;top:297px">18</div><div class="cal-day" style="left:514px;top:297px">19</div><div class="cal-day" style="left:562px;top:297px">20</div><div class="cal-day" style="left:610px;top:297px">21</div><div class="cal-day" style="left:656px;top:300px">22</div>
      <div class="cal-day" style="left:373px;top:340px">23</div><div class="cal-day" style="left:420px;top:340px">24</div><div class="cal-day avail" style="left:468px;top:340px">25</div><div class="cal-day avail" style="left:514px;top:340px">26</div><div class="cal-day picked" style="left:562px;top:340px">27</div><div class="cal-day" style="left:610px;top:340px">28</div><div class="cal-day" style="left:656px;top:343px">29</div>
      <div class="cal-day avail" style="left:373px;top:383px">30</div>
      <p class="abs" style="left:356px;top:428px;font-size:14px;color:#333">Time Zone</p>
      <p class="abs" style="left:356px;top:455px;font-size:12px;color:#555">◍ &nbsp;America/Adak (8:38pm) &nbsp;⌄</p>

      <div class="slot" style="top:122px">3:30pm</div>
      <div class="slot" style="top:178px">4:00pm</div>
      <div class="slot" style="top:232px">4:30pm</div>
      <div class="slot" style="top:288px;width:72px;background:var(--blue);color:#fff">5:00pm</div>
      <div class="slot" style="top:288px;left:783px;width:76px;background:var(--teal);border-color:var(--teal);color:#fff">Next</div>
      <div class="slot" style="top:342px">5:30pm</div>
      <div class="slot" style="top:397px">6:00pm</div>
      <div class="slot" style="top:453px">4:30pm</div>
      <span class="abs" style="left:881px;top:177px;width:3px;height:172px;background:#c7ccd4"></span>
    </div>
  </div>

  <!-- partners -->
  <div class="abs partner" style="left:227px">Meridan</div>
  <div class="abs partner" style="left:426px"><i></i>Corvalis</div>
  <div class="abs partner" style="left:666px">Haulmark</div>
  <div class="abs partner" style="left:855px"><i style="width:20px;height:20px;border-radius:50%"></i>Solvara</div>

  <!-- footer -->
  <footer class="abs footer"></footer>
  <h3 class="abs news-head" style="font-weight:400">Australia's Largest health charity<br>implements Quarvendo API Msg Bus</h3>
  <p class="abs news-reg">Register to our newsletter to find out more.</p>
  <div class="abs email">Enter your email</div>
  <div class="abs subscribe">SUBSCRIBE</div>
  <div class="abs rule"></div>
  <div class="abs brand" style="left:466px;top:3748px;font-size:34px"><span class="brand-mark" style="width:48px;height:48px"></span>quarvendo</div>
  <div class="abs social" style="left:523px">f</div>
  <div class="abs social" style="left:577px">t</div>
  <div class="abs social" style="left:632px">in</div>
  <p class="abs small" style="left:88px;top:3938px">© Copyright quarvendo, All Rights Reserved</p>
  <p class="abs small" style="left:928px;top:3938px">Contact Us</p>
  <p class="abs small" style="left:1027px;top:3938px">Privacy Policy</p>
  <svg class="abs" style="left:1134px;top:3890px" width="40" height="38" viewBox="0 0 40 38"><path d="M20 3C10 3 3 9 3 17c0 4 2 8 6 10l-2 8 9-6c1 0 3 1 4 1 10 0 17-6 17-13S30 3 20 3z" fill="var(--teal)"/><circle cx="13" cy="17" r="2" fill="#fff"/><circle cx="20" cy="17" r="2" fill="#fff"/><circle cx="27" cy="17" r="2" fill="#fff"/></svg>

</div>
</body>
</html>
```